Updated DJ business Card showing other businesses

DJ Kestro offers professional mobile dj services including DJ. MC. Karaoke.
Silent Disco (will attach logo)
I also offer a 360 Photo Booth.

Contact info:
(555) 314-7720
lenny.corbitt@mailvane.net
Social Media @DJKestroBPZ

```html
<!DOCTYPE html>
<html lang="en">
<head>
<meta charset="utf-8">
<title>DJ Kestro – Business Card</title>
<link rel="stylesheet" href="https://fonts.googleapis.com/css2?family=Montserrat:wght@400;500;700;800&display=swap">
<style>
  :root {
    --backdrop: #3b3b3d;
    --card-white: #ffffff;
    --card-black: #0d0d0e;
    --accent-red: #f0194a;
    --ink: #111111;
    --paper-text: #f4f4f4;
  }
  * { box-sizing: border-box; margin: 0; padding: 0; }
  html, body {
    width: 1200px; height: 1200px; overflow: hidden;
    background: var(--backdrop);
    font-family: "Montserrat", sans-serif;
  }
  .sheet {
    width: 1200px; height: 1200px;
    display: flex; flex-direction: column; align-items: center; justify-content: center;
    gap: 36px;
  }
  .card {
    position: relative;
    width: 960px; height: 548px;
    border-radius: 40px;
    overflow: hidden;
    box-shadow: 0 18px 40px rgba(0,0,0,.45);
  }

  /* Front */
  .card--front { background: var(--card-black); }
  .front__top {
    position: absolute; left: 0; top: 0; width: 100%; height: 318px;
    background: var(--card-white);
    display: flex; align-items: center; justify-content: center;
  }
  .front__rule {
    position: absolute; left: 0; top: 302px; width: 100%; height: 9px;
    background: var(--accent-red);
  }
  .brand-name {
    font-weight: 800;
    font-size: 128px;
    letter-spacing: -2px;
    line-height: 1;
    text-transform: uppercase;
  }
  .front__top .brand-name { color: var(--ink); margin-top: -20px; }

  .contacts {
    position: absolute; right: 52px; top: 346px;
    list-style: none;
    color: var(--paper-text);
    font-size: 25px; font-weight: 400;
    display: flex; flex-direction: column; gap: 10px;
  }
  .contacts li { display: flex; align-items: center; gap: 12px; }
  .contacts svg { width: 26px; height: 26px; flex: none; }

  .services {
    position: absolute; left: 56px; bottom: 44px;
    color: var(--paper-text);
    font-weight: 500; font-size: 30px; line-height: 1.2;
    text-transform: uppercase;
  }
  .services .dot { color: var(--accent-red); padding: 0 6px; }

  /* Back */
  .card--back {
    background: var(--card-black);
    display: flex; flex-direction: column; align-items: center; justify-content: center;
    gap: 34px;
  }
  .card--back .brand-name { color: var(--paper-text); font-size: 140px; }
  .partner {
    display: flex; align-items: center; gap: 14px;
    color: var(--paper-text);
    font-weight: 700; font-size: 34px; text-transform: uppercase;
    align-self: flex-end; margin-right: 170px;
  }
  .partner__mark {
    width: 40px; height: 40px; border-radius: 50%;
    border: 3px solid var(--paper-text);
  }
</style>
</head>
<body>
<main class="sheet">

  <section class="card card--front" aria-label="Business card front">
    <div class="front__top">
      <h1 class="brand-name">DJ Kestro</h1>
    </div>
    <div class="front__rule"></div>

    <ul class="contacts">
      <li>
        <svg viewBox="0 0 24 24" aria-hidden="true"><path fill="#f0194a" d="M6.6 10.8a15.1 15.1 0 0 0 6.6 6.6l2.2-2.2c.3-.3.7-.4 1-.2 1.1.4 2.3.6 3.6.6.6 0 1 .4 1 1V20c0 .6-.4 1-1 1A17 17 0 0 1 3 4c0-.6.4-1 1-1h3.5c.6 0 1 .4 1 1 0 1.3.2 2.5.6 3.6.1.3 0 .7-.2 1l-2.3 2.2z"/></svg>
        <span>(555) 314-7720</span>
      </li>
      <li>
        <svg viewBox="0 0 24 24" aria-hidden="true"><rect x="2" y="5" width="20" height="14" rx="1.5" fill="#f0194a"/><path d="M2.5 6l9.5 7 9.5-7" fill="none" stroke="#0d0d0e" stroke-width="1.6"/></svg>
        <span>lenny.corbitt@mailvane.net</span>
      </li>
      <li>
        <svg viewBox="0 0 24 24" aria-hidden="true"><rect x="3" y="3" width="18" height="18" rx="4" fill="none" stroke="#f0194a" stroke-width="2"/></svg>
        <span>@DJKestroBPZ</span>
      </li>
    </ul>

    <p class="services">
      Mobile DJ Services<br>
      DJ<span class="dot">•</span>MC<span class="dot">•</span>Karaoke<br>
      360 Photo Booth
    </p>
  </section>

  <section class="card card--back" aria-label="Business card back">
    <h2 class="brand-name">DJ Kestro</h2>
    <div class="partner">
      <span class="partner__mark" aria-hidden="true"></span>
      <span>Silent Disco</span>
    </div>
  </section>

</main>
</body>
</html>
```